Quarrel Engineering Business Card Design

We need a new business card for our engineering consultancy, Quarrel Engineering. The card should look sharp and professional.

Quarrel Engineering is mechanical engineering consultancy providing engineering services and testing. We mainly serve the automotive enthusiast (certifying modified vehicles) and trade sectors (product development & certification). The company also provides general mechanical engineering consultancy, and services to the railway industry.

The logo attached should be used.

Location: Adelaide, South Australia

Target Market(s)

Individual Clients, and corporate clients

Industry/Entity Type

Mechanical Engineering

Requirements
Must have
• Front:

Quarrel Engineering Pty Ltd
PO Box 417
Hollowmere, SA 5093

Gareth Lunsmore MBA,BEng(Mech), MIEAust CPEng
glunsmore@quarrelengineering.com.au
quarrelengineering.com.au
mobile +61 (0)400 183 947

Back
Modified Vehicle Engineering & Testing
Component Design & Analysis
Individually Constructed Vehicle Engineering
Australian Design Rule (ADR) Compliance Testing
General Mechanical Engineering
Permanent Way Engineering Services
Rail Plant and Equipment Services

Nice to have
• embossing
Should not have
• Photographs or images other than the logo.

```html
<!DOCTYPE html>
<html lang="en">
<head>
<meta charset="utf-8">
<title>Quarrel Engineering Business Card</title>
<link rel="stylesheet" href="https://fonts.googleapis.com/css2?family=Michroma&family=Exo+2:wght@400;500&display=swap">
<style>
  :root {
    --backdrop: #d9d9db;
    --card-white: #f1f1f2;
    --card-grey: #e4e4e6;
    --ink-navy: #1c2a4a;
    --brand-blue: #3a78c4;
    --panel-light: #8fbde6;
    --panel-deep: #4a8ccd;
    --edge-navy: #13254a;
  }
  * { box-sizing: border-box; margin: 0; padding: 0; }
  html, body { width: 1200px; height: 750px; overflow: hidden; }
  body {
    background: var(--backdrop);
    font-family: "Exo 2", sans-serif;
    color: var(--ink-navy);
    display: flex;
    align-items: center;
    justify-content: center;
    gap: 40px;
  }
  .card {
    position: relative;
    width: 520px;
    height: 318px;
    border-radius: 22px;
    overflow: hidden;
    background: var(--card-white);
    box-shadow: 0 6px 18px rgba(0,0,0,.18);
  }

  /* Front */
  .card--front .panel { position: absolute; inset: 0; width: 100%; height: 100%; }
  .brand {
    display: flex;
    align-items: center;
    gap: 8px;
    white-space: nowrap;
  }
  .brand--front {
    position: absolute;
    left: 28px;
    top: 252px;
  }
  .brand__dot {
    width: 16px; height: 16px; border-radius: 50%;
    background: var(--brand-blue);
    flex: none;
  }
  .brand__name {
    font-family: "Michroma", sans-serif;
    font-size: 12px;
    color: var(--ink-navy);
    text-transform: uppercase;
    letter-spacing: .3px;
  }
  .contact {
    position: absolute;
    right: 26px;
    top: 22px;
    text-align: right;
    color: var(--ink-navy);
    white-space: nowrap;
  }
  .contact__company {
    font-family: "Michroma", sans-serif;
    font-size: 9px;
    text-transform: uppercase;
  }
  .contact__address { font-size: 11px; line-height: 1.35; margin-top: 3px; }
  .contact__name {
    font-family: "Michroma", sans-serif;
    font-size: 16px;
    font-variant: small-caps;
    margin-top: 18px;
  }
  .contact__quals { font-size: 9.5px; margin-top: 1px; }
  .contact__line {
    display: flex; align-items: center; justify-content: flex-end;
    gap: 5px; font-size: 10px; margin-top: 4px;
  }
  .contact__icon { width: 12px; height: 12px; flex: none; }

  /* Back */
  .card--back { background: linear-gradient(135deg, var(--card-grey), var(--card-white)); }
  .brand--back {
    position: absolute;
    right: 30px;
    top: 34px;
  }
  .brand--back .brand__dot { width: 20px; height: 20px; }
  .brand--back .brand__name { font-size: 15px; }
  .back__services {
    position: absolute;
    left: 26px; right: 26px; top: 122px;
    display: flex;
    justify-content: space-between;
    gap: 12px;
  }
  .service-list { list-style: none; font-size: 11px; line-height: 1.65; white-space: nowrap; }
  .service-list--right { text-align: right; }
  .back__wide {
    position: absolute;
    left: 26px; right: 26px; bottom: 40px;
    font-size: 12.5px;
    text-align: center;
  }
</style>
</head>
<body>

  <section class="card card--front" aria-label="Card front">
    <svg class="panel" viewBox="0 0 520 318" preserveAspectRatio="none" aria-hidden="true">
      <defs>
        <linearGradient id="panelFill" x1="0" y1="0" x2="1" y2="1">
          <stop offset="0" stop-color="#8fbde6"/>
          <stop offset="1" stop-color="#4a8ccd"/>
        </linearGradient>
      </defs>
      <path d="M225,0 C275,70 240,220 330,318 L520,318 L520,0 Z" fill="url(#panelFill)"/>
      <path d="M225,0 C275,70 240,220 330,318" fill="none" stroke="#13254a" stroke-width="7"/>
    </svg>

    <div class="brand brand--front">
      <span class="brand__dot"></span>
      <span class="brand__name">Quarrel Engineering</span>
    </div>

    <div class="contact">
      <p class="contact__company">Quarrel Engineering Pty Ltd</p>
      <p class="contact__address">PO Box 417<br>Hollowmere, SA 5093</p>
      <p class="contact__name">Gareth Lunsmore</p>
      <p class="contact__quals">MBA,BEng(Mech), MIEAust CPEng</p>
      <p class="contact__line">glunsmore@quarrelengineering.com.au
        <svg class="contact__icon" viewBox="0 0 16 16" aria-hidden="true"><circle cx="8" cy="8" r="7" fill="none" stroke="#1c2a4a"/><rect x="4" y="5.5" width="8" height="5" fill="none" stroke="#1c2a4a"/><path d="M4 5.5 L8 8.5 L12 5.5" fill="none" stroke="#1c2a4a"/></svg>
      </p>
      <p class="contact__line">quarrelengineering.com.au
        <svg class="contact__icon" viewBox="0 0 16 16" aria-hidden="true"><circle cx="8" cy="8" r="7" fill="none" stroke="#1c2a4a"/><circle cx="8" cy="8" r="3.5" fill="none" stroke="#1c2a4a"/><path d="M4.5 8 H11.5" stroke="#1c2a4a"/></svg>
      </p>
      <p class="contact__line">+61 (0)400 183 947
        <svg class="contact__icon" viewBox="0 0 16 16" aria-hidden="true"><circle cx="8" cy="8" r="7" fill="none" stroke="#1c2a4a"/><rect x="5.5" y="3.5" width="5" height="9" rx="1" fill="none" stroke="#1c2a4a"/><circle cx="8" cy="11" r=".7" fill="#1c2a4a"/></svg>
      </p>
    </div>
  </section>

  <section class="card card--back" aria-label="Card back">
    <div class="brand brand--back">
      <span class="brand__dot"></span>
      <span class="brand__name">Quarrel Engineering</span>
    </div>
    <div class="back__services">
      <ul class="service-list">
        <li>Component Design &amp; Analysis</li>
        <li>Permanent Way Engineering Services</li>
        <li>Modified Vehicle Engineering &amp; Testing</li>
      </ul>
      <ul class="service-list service-list--right">
        <li>General Mechanical Engineering</li>
        <li>Rail Plant and Equipment Services</li>
        <li>Individually Constructed Vehicle Engineering</li>
      </ul>
    </div>
    <p class="back__wide">Australian Design Rule (ADR) Compliance Testing</p>
  </section>

</body>
</html>
```